Get your icon design on millions of orbitan phones

We're looking for app icon for an orbitan app which provides backup, transfer and recover. App saves data to cloud (Cratevault, Ledger, Vyn etc)) and maintains timeline of activity - so you can go back to snapshot at previous date.
Themes - backup transfer recover, save to cloud.
Also, we're looking for an icon set for categories that are included in backup operation:-
Messages,
Call log,
Photos,
Videos
Contacts
Music
Settings
These icons will have badges applied to indicate status. Sample using orbitan QELT icons as per attached screenshot image. (Different brands use their own stylised icons for apps such as messages). Also as per screenshot the icons can be monochromed to show disabled state. So, icons that fill required. See sample kirovel icons attached - we'll apply badges on top left or top right. e.g. green tick in top left corner for all data safe. Items count in top right if there are changes to upload.
Target Market(s)
People who care about losing details on their phone such as call log, messages, photos. More often 30-45 year old males who buy an expensive smartphone.
Industry/Entity Type
Orbitan
Look and feel

```html
<!DOCTYPE html>
<html lang="en">
<head>
<meta charset="utf-8">
<title>Backup Category Icons and App Icon</title>
<link rel="stylesheet" href="https://fonts.googleapis.com/css2?family=Roboto:wght@400;500;700&family=Source+Sans+3:wght@400&display=swap">
<style>
  :root {
    --ink: #111111;
    --label: #1a1a1a;
    --page: #ffffff;
    --bar-black: #000000;
    --action-bar: #222222;
    --divider: #3c3c3c;
    --row-bg: #ffffff;
    --row-shadow: #d4d4d4;
    --row-text: #333333;
    --track: #e3e3e3;
    --accent: #1ea7d8;
    --accent-deep: #1590c2;
    --status-blue: #33b5e5;
    --silver-light: #f4f5f6;
    --silver-dark: #b9bcc0;
  }
  * { box-sizing: border-box; margin: 0; padding: 0; }
  html, body {
    width: 1200px; height: 850px; overflow: hidden;
    background: var(--page);
  }
  .canvas {
    position: relative; width: 1200px; height: 850px; overflow: hidden;
  }
  .board {
    position: absolute; left: 0; top: 0;
    width: 1220px; height: 864px;
    transform: scale(0.9836); transform-origin: 0 0;
    font-family: "Source Sans 3", sans-serif;
    color: var(--ink);
  }
  .glyph { position: absolute; fill: var(--ink); color: var(--ink); }
  .cat-label {
    position: absolute; width: 100px; margin-left: -50px;
    text-align: center; font-size: 15px; line-height: 18px; color: var(--label);
  }
  .alt-or {
    position: absolute; width: 30px; margin-left: -15px;
    text-align: center; font-size: 10px; line-height: 12px; font-style: italic; color: var(--label);
  }

  /* Phone screen */
  .screen {
    position: absolute; left: 345px; top: 0; width: 485px; height: 864px;
    background: linear-gradient(#ffffff 0, #ffffff 600px, #f6f6f6 700px, #ffffff 790px);
    font-family: "Roboto", sans-serif;
  }
  .status-bar {
    height: 35px; background: var(--bar-black);
    display: flex; justify-content: flex-end; align-items: center; gap: 8px;
    padding-right: 10px; color: var(--status-blue); font-size: 20px;
  }
  .action-bar {
    height: 63px; background: var(--action-bar);
    display: flex; align-items: center; position: relative;
    box-shadow: 0 2px 3px rgba(0,0,0,.35);
  }
  .action-done {
    display: flex; align-items: center; gap: 14px; padding-left: 20px;
    color: #fff; font-weight: 700; font-size: 15px; letter-spacing: .3px;
    height: 100%;
  }
  .action-divider { position: absolute; left: 155px; top: 15px; width: 1px; height: 33px; background: var(--divider); }
  .overflow-menu { position: absolute; right: 32px; top: 17px; }
  .overflow-menu span { display: block; width: 6px; height: 6px; background: #8a8a8a; margin-bottom: 4px; }
  .category-list { list-style: none; position: absolute; top: 100px; left: 7px; width: 470px; }
  .category-row {
    height: 78px; margin-bottom: 3px; background: var(--row-bg);
    border-bottom: 2px solid var(--row-shadow);
    display: flex; align-items: center; position: relative;
  }
  .row-icon { position: absolute; left: 14px; width: 48px; height: 48px; fill: var(--ink); color: var(--ink); }
  .row-name { position: absolute; left: 81px; font-size: 18px; color: var(--row-text); }
  .toggle {
    position: absolute; left: 331px; width: 130px; height: 31px;
    background: var(--track); box-shadow: inset 0 1px 2px rgba(0,0,0,.12);
  }
  .toggle-on {
    position: absolute; right: 1px; top: 2px; width: 62px; height: 27px;
    background: var(--accent); color: #fff; font-size: 16px;
    display: flex; align-items: center; justify-content: center;
  }
  .nav-bar {
    position: absolute; bottom: 0; left: 0; width: 100%; height: 64px;
    background: var(--bar-black);
  }

  /* App icon areas */
  .app-icon-framed {
    position: absolute; left: 874px; top: 62px; width: 346px; height: 346px;
    border-radius: 70px;
    background: linear-gradient(var(--silver-light), var(--silver-dark));
    padding: 20px;
  }
  .app-icon-tile {
    width: 100%; height: 100%; border-radius: 54px;
    background: linear-gradient(#21abd9, var(--accent-deep));
  }
  .app-icon-plain {
    position: absolute; left: 875px; top: 458px; width: 345px; height: 345px;
    border-radius: 62px;
    background: linear-gradient(#bfe6f2 0, #27b0dd 12%, var(--accent-deep) 100%);
  }
</style>
</head>
<body>
<svg width="0" height="0" style="position:absolute" aria-hidden="true">
  <defs>
    <symbol id="icon-envelope" viewBox="0 0 48 36">
      <rect x="1.5" y="1.5" width="45" height="33" fill="none" stroke="currentColor" stroke-width="2.6"/>
      <path d="M2 3 L24 21 L46 3 M2 33 L18 17 M46 33 L30 17" fill="none" stroke="currentColor" stroke-width="2.6"/>
    </symbol>
    <symbol id="icon-envelope-open" viewBox="0 0 48 44">
      <path d="M0 16 L24 0 L48 16 V44 H0 Z"/>
      <path d="M2 18 L24 34 L46 18 M2 42 L19 28 M46 42 L29 28" fill="none" stroke="#fff" stroke-width="2.6"/>
    </symbol>
    <symbol id="icon-handset" viewBox="0 0 40 48">
      <path d="M9 1 C4 3 0 7 1 14 C3 27 13 40 26 46 C31 48 36 46 38 42 L30 33 C27 35 24 36 22 34 C17 30 13 23 11 17 C10 14 12 12 14 11 Z"/>
      <path d="M10 0 L17 10 L14 12 L7 2 Z M31 32 L39 41 L36 44 L28 35 Z"/>
    </symbol>
    <symbol id="icon-photos" viewBox="0 0 48 36">
      <rect x="1.5" y="1.5" width="36" height="24" fill="#fff" stroke="currentColor" stroke-width="2"/>
      <rect x="9.5" y="9.5" width="37" height="25" fill="#fff" stroke="currentColor" stroke-width="2"/>
      <path d="M13 31 L22 21 L28 27 L34 20 L43 31 Z"/>
      <circle cx="37" cy="15" r="2.5"/>
    </symbol>
    <symbol id="icon-camera" viewBox="0 0 48 44">
      <circle cx="9" cy="6" r="5"/><circle cx="21" cy="6" r="5"/>
      <rect x="2" y="10" width="30" height="17"/>
      <path d="M32 16 L46 10 V27 L32 21 Z"/>
      <path d="M17 27 L9 44 M17 27 L25 44 M17 27 V44" fill="none" stroke="currentColor" stroke-width="2.6"/>
    </symbol>
    <symbol id="icon-play" viewBox="0 0 44 44">
      <circle cx="22" cy="22" r="19.5" fill="none" stroke="currentColor" stroke-width="4"/>
      <path d="M16 11 L33 22 L16 33 Z"/>
    </symbol>
    <symbol id="icon-film" viewBox="0 0 38 48">
      <path fill-rule="evenodd" d="M0 0 H38 V48 H0 Z M10 4 V44 H28 V4 Z M3 3 V7 H7 V3 Z M3 11 V15 H7 V11 Z M3 19 V23 H7 V19 Z M3 27 V31 H7 V27 Z M3 35 V39 H7 V35 Z M3 42 V46 H7 V42 Z M31 3 V7 H35 V3 Z M31 11 V15 H35 V11 Z M31 19 V23 H35 V19 Z M31 27 V31 H35 V27 Z M31 35 V39 H35 V35 Z M31 42 V46 H35 V42 Z"/>
    </symbol>
    <symbol id="icon-music" viewBox="0 0 40 44">
      <path d="M13 8 L38 0 V7 L13 15 Z"/>
      <path d="M13 9 V36 M36 2 V30" stroke="currentColor" stroke-width="3"/>
      <ellipse cx="8" cy="36" rx="6.5" ry="5" transform="rotate(-20 8 36)"/>
      <ellipse cx="31" cy="30" rx="6.5" ry="5" transform="rotate(-20 31 30)"/>
    </symbol>
    <symbol id="icon-contacts" viewBox="0 0 42 48">
      <rect x="1.5" y="1.5" width="39" height="45" rx="4" fill="none" stroke="currentColor" stroke-width="3"/>
      <path d="M4 5 H38" stroke="currentColor" stroke-width="2"/>
      <rect x="10" y="11" width="22" height="26" fill="none" stroke="currentColor" stroke-width="2"/>
      <circle cx="21" cy="21" r="4.5"/>
      <path d="M13 34 C13 28 17 26 21 26 C25 26 29 28 29 34 Z"/>
    </symbol>
    <symbol id="icon-mic" viewBox="0 0 32 48">
      <rect x="8" y="0" width="16" height="28" rx="8"/>
      <path d="M11 5 V18 M14 3 V18 M18 3 V18 M21 5 V18" stroke="#fff" stroke-width="1.4"/>
      <path d="M3 18 V21 C3 28 9 33 16 33 C23 33 29 28 29 21 V18" fill="none" stroke="currentColor" stroke-width="3"/>
      <path d="M16 33 V43" stroke="currentColor" stroke-width="3"/>
      <rect x="7" y="42" width="18" height="5" rx="1"/>
    </symbol>
    <symbol id="icon-gears" viewBox="0 0 48 42">
      <circle cx="17" cy="17" r="11" fill="none" stroke="currentColor" stroke-width="7" stroke-dasharray="4.6 3.5"/>
      <circle cx="17" cy="17" r="9.5" fill="none" stroke="currentColor" stroke-width="5"/>
      <circle cx="36" cy="30" r="6.8" fill="none" stroke="currentColor" stroke-width="5" stroke-dasharray="3.2 2.8"/>
      <circle cx="36" cy="30" r="5.6" fill="none" stroke="currentColor" stroke-width="3.6"/>
    </symbol>
  </defs>
</svg>

<div class="canvas">
<main class="board">
  <!-- Category icon set -->
  <section class="icon-set">
    <svg class="glyph" style="left:5px;top:177px;width:48px;height:44px"><use href="#icon-envelope-open"/></svg>
    <div class="alt-or" style="left:30px;top:227px">or</div>
    <svg class="glyph" style="left:6px;top:251px;width:48px;height:36px"><use href="#icon-envelope"/></svg>
    <div class="cat-label" style="left:30px;top:299px">Message</div>

    <svg class="glyph" style="left:100px;top:244px;width:40px;height:48px"><use href="#icon-handset"/></svg>
    <div class="cat-label" style="left:120px;top:299px">Call Log</div>

    <svg class="glyph" style="left:189px;top:251px;width:48px;height:36px"><use href="#icon-photos"/></svg>
    <div class="cat-label" style="left:212px;top:299px">Photos</div>

    <svg class="glyph" style="left:281px;top:106px;width:44px;height:44px"><use href="#icon-play"/></svg>
    <div class="alt-or" style="left:303px;top:157px">or</div>
    <svg class="glyph" style="left:285px;top:175px;width:38px;height:48px"><use href="#icon-film"/></svg>
    <div class="alt-or" style="left:303px;top:228px">or</div>
    <svg class="glyph" style="left:280px;top:248px;width:48px;height:44px"><use href="#icon-camera"/></svg>
    <div class="cat-label" style="left:303px;top:299px">Videos</div>

    <svg class="glyph" style="left:148px;top:346px;width:40px;height:44px"><use href="#icon-music"/></svg>
    <div class="alt-or" style="left:167px;top:398px">or</div>
    <svg class="glyph" style="left:151px;top:415px;width:32px;height:48px"><use href="#icon-mic"/></svg>
    <div class="cat-label" style="left:167px;top:469px">Audio/Music</div>

    <svg class="glyph" style="left:53px;top:415px;width:42px;height:48px"><use href="#icon-contacts"/></svg>
    <div class="cat-label" style="left:76px;top:469px">Contacts</div>

    <svg class="glyph" style="left:234px;top:419px;width:48px;height:42px"><use href="#icon-gears"/></svg>
    <div class="cat-label" style="left:258px;top:469px">Setting</div>
  </section>

  <!-- Backup settings screen -->
  <section class="screen">
    <div class="status-bar">
      <svg width="26" height="20" viewBox="0 0 26 20"><path d="M13 20 L0 6 C7 -1 19 -1 26 6 Z" fill="var(--status-blue)"/></svg>
      <svg width="12" height="22" viewBox="0 0 12 22"><rect x="3" y="0" width="6" height="3" fill="var(--status-blue)"/><rect x="0" y="2" width="12" height="20" rx="1" fill="var(--status-blue)"/><path d="M7 5 L3 13 H6 L5 19 L9 10 H6 Z" fill="#000"/></svg>
      <span>6:28</span>
    </div>
    <div class="action-bar">
      <div class="action-done">
        <svg width="34" height="26" viewBox="0 0 34 26"><path d="M2 13 L12 23 L32 2" fill="none" stroke="#fff" stroke-width="2.4"/></svg>
        <span>DONE</span>
      </div>
      <div class="action-divider"></div>
      <div class="overflow-menu"><span></span><span></span><span></span></div>
    </div>

    <ul class="category-list">
      <li class="category-row">
        <svg class="row-icon" viewBox="0 0 40 48" style="left:19px;width:38px"><use href="#icon-handset"/></svg>
        <span class="row-name">Calls</span>
        <div class="toggle"><div class="toggle-on">ON</div></div>
      </li>
      <li class="category-row">
        <svg class="row-icon" viewBox="0 0 42 48" style="left:17px;width:42px"><use href="#icon-contacts"/></svg>
        <span class="row-name">Contacts</span>
        <div class="toggle"><div class="toggle-on">ON</div></div>
      </li>
      <li class="category-row">
        <svg class="row-icon" viewBox="0 0 48 36" style="left:14px;height:36px"><use href="#icon-envelope"/></svg>
        <span class="row-name">Messagaes</span>
        <div class="toggle"><div class="toggle-on">ON</div></div>
      </li>
      <li class="category-row">
        <svg class="row-icon" viewBox="0 0 48 36" style="left:14px;height:36px"><use href="#icon-photos"/></svg>
        <span class="row-name">Photos</span>
        <div class="toggle"><div class="toggle-on">ON</div></div>
      </li>
      <li class="category-row">
        <svg class="row-icon" viewBox="0 0 48 44" style="left:14px;height:44px"><use href="#icon-camera"/></svg>
        <span class="row-name">Videos</span>
        <div class="toggle"><div class="toggle-on">ON</div></div>
      </li>
      <li class="category-row">
        <svg class="row-icon" viewBox="0 0 32 48" style="left:22px;width:32px"><use href="#icon-mic"/></svg>
        <span class="row-name">Audio</span>
        <div class="toggle"><div class="toggle-on">ON</div></div>
      </li>
    </ul>

    <div class="nav-bar">
      <svg width="485" height="64" viewBox="0 0 485 64">
        <path d="M88 28 L94 22 M88 28 L94 34 M88 28 H122 C127 28 128 32 128 34 C128 38 125 40 122 40 H110" fill="none" stroke="#8c8c8c" stroke-width="2.4"/>
        <path d="M220 42 V30 L242 22 L264 30 V42 Z" fill="none" stroke="#8c8c8c" stroke-width="2.4"/>
        <rect x="357" y="31" width="30" height="12" fill="none" stroke="#8c8c8c" stroke-width="2.4"/>
        <path d="M361 28 V25 H393 V37 H390" fill="none" stroke="#8c8c8c" stroke-width="2.4"/>
      </svg>
    </div>
  </section>

  <!-- App icon placeholders -->
  <div class="app-icon-framed">
    <div class="app-icon-tile" role="img" aria-label="App logo mark on blue tile with silver frame"></div>
  </div>
  <div class="app-icon-plain" role="img" aria-label="App logo mark on blue tile"></div>
</main>
</div>
</body>
</html>
```